Brise De Lavande is a restaurant and we would like to redesign our old menu.,

Our restaurant menu, ideal for brunch or lunch, showcases French bakery and cafe delights, including quiches, soups, and grown-up grilled cheese. Join us for a culinary journey through France without leaving Marietta, where every bite reflects our passion for quality, tradition, and the joy of French cuisine. Your taste buds will delight in every bite! this Menu Size is 11x 17 tri fold

Target Market(s)

Older Guest 35 to 65

Industry/Entity Type

Food Restaurant

Font styles to use
Serif
Decorative

Colors
0054AA
0677BA
7BADD7
CADEEF
E8F1F8
EB3D1F
EC4F4E
F09395
F8D3D4
FCEDEE

Requirements
Must have
• Larger print to be easier to read but not too large. , 11 x 17 trifold
Nice to have
• I want this menu to be blue as a background and either red as the complementary color or gold

```html
<!DOCTYPE html>
<html lang="en">
<head>
<meta charset="utf-8">
<title>Brise De Lavande – French Bakery and Cafe Menu</title>
<link href="https://fonts.googleapis.com/css2?family=Fjalla+One&family=Yellowtail&family=Poppins:wght@400;600;700;800&display=swap" rel="stylesheet">
<style>
:root{
  --navy:#1f1e63;
  --ink:#1c2560;
  --blue:#0054aa;
  --blue-mid:#0677ba;
  --blue-light:#7badd7;
  --blue-pale:#cadeef;
  --red:#eb3d1f;
  --red-soft:#ec4f4e;
  --white:#ffffff;
  --desc:#d8def2;
  --stage:#f2f2f2;
}
*{margin:0;padding:0;box-sizing:border-box}
html,body{width:750px;height:1200px;overflow:hidden;background:var(--stage)}
body{position:relative;font-family:"Poppins",sans-serif;color:var(--white)}
.panel{position:absolute;width:560px;height:1117px;transform:scale(.496);transform-origin:0 0;overflow:hidden;background:var(--navy)}
.panel--breakfast{left:90px;top:38px}
.panel--lunch{left:382px;top:38px}
.panel--drinks{left:236px;top:608px}
.masthead{position:absolute;left:0;top:0;width:560px;height:135px;background:linear-gradient(115deg,#f4f5f6 0%,#dfe2e5 25%,#fbfbfc 45%,#e3e6e9 70%,#f7f8f9 100%)}
.brand-mark{position:absolute;left:136px;top:40px;width:34px;height:34px;background:var(--ink)}
.brand-name{position:absolute;left:40px;top:98px;width:230px;text-align:center;font-family:"Poppins",sans-serif;font-weight:400;font-size:13px;letter-spacing:5.5px;color:var(--ink);text-transform:uppercase}
.title{position:absolute;left:238px;top:28px;width:290px;text-align:center;font-family:"Fjalla One",sans-serif;line-height:44px}
.title .l1{display:block;font-size:47px;color:var(--ink)}
.title .l2{display:block;font-size:47px;color:var(--blue)}
.band{position:absolute;left:0;top:135px;width:560px;height:18px;background:linear-gradient(180deg,var(--blue) 0%,var(--blue-mid) 45%,var(--blue-light) 60%,var(--navy) 100%)}
.frame{position:absolute;border:2px solid var(--white)}
.script{position:absolute;font-family:"Yellowtail",cursive;font-weight:400;color:var(--red);font-size:34px;line-height:34px;background:var(--navy);padding:0 14px;transform:translate(-50%,-50%);white-space:nowrap}
.script--plain{background:none;padding:0;transform:translateY(-50%)}
.it{position:absolute;width:211px}
.it h4{display:flex;justify-content:space-between;font-size:11.5px;line-height:12.5px;font-weight:700;gap:6px}
.it h4 span:last-child{text-align:right;white-space:nowrap}
.it p{font-size:9.6px;line-height:12.6px;color:var(--desc)}
.it p b{font-weight:700;color:var(--white)}
.it .sub{display:flex;gap:5px}
.it .sub b{white-space:nowrap}
.stack{position:absolute;display:flex;flex-direction:column;gap:9px}
.stack .it{position:static;width:100%}
.stack .it p{font-size:9.2px;line-height:11.8px}
.waves{position:absolute;left:0;top:940px;width:560px;height:140px}
.fine{position:absolute;left:0;top:1066px;width:560px;text-align:center;font-size:7.4px;line-height:11.5px;color:var(--desc)}
.photo{position:absolute}
.photo--pie{left:284px;top:153px;width:276px;height:241px;background:radial-gradient(ellipse at 50% 45%,#e3b563 0%,#c98f3f 40%,#6b4a32 75%,#2d2a33 100%)}
.photo--panini{left:52px;top:627px;width:210px;height:112px;background:linear-gradient(135deg,#6b5a3a 0%,#d8b57c 40%,#c0432f 60%,#7fa341 85%)}
.photo--wine{left:52px;top:493px;width:208px;height:100px;background:linear-gradient(120deg,#2f3a1d 0%,#6e7d3a 40%,#e1d28e 60%,#3d2a3c 100%)}
.photo--juice{left:297px;top:828px;width:211px;height:135px;background:linear-gradient(120deg,#f2c21d 0%,#f08a2a 35%,#9bc24d 60%,#c0304a 100%)}
.side{position:absolute;left:52px;width:203px;display:flex;justify-content:space-between;gap:6px;font-size:11.5px;line-height:12.6px}
.side b{font-weight:700}
.kids-head{position:absolute;left:297px;top:764px;display:flex;align-items:center;gap:12px}
.kids-head .script{position:static;transform:none;background:none;padding:0}
.kids-price{flex:none;width:52px;height:52px;border-radius:50%;background:var(--red);color:var(--white);font-weight:800;font-size:28px;line-height:52px;text-align:center}
.kids-list{position:absolute;left:297px;top:824px;list-style:none;font-size:12.3px;line-height:20.1px}
.head{position:absolute;font-weight:800;font-size:17.5px;color:var(--red);letter-spacing:.2px;line-height:18px}
.head--center{transform:translateX(-50%);background:var(--navy);padding:0 10px;white-space:nowrap}
.rule{position:absolute;height:2px;width:44px;background:var(--white)}
.wine{position:absolute;left:52px;width:212px;font-size:9.8px;line-height:12.6px}
.wine .row{display:grid;grid-template-columns:1fr 30px 32px;align-items:start}
.wine .row span:nth-child(n+2){text-align:right;font-weight:600}
.wine .cols span{font-weight:700;font-size:9.4px}
.list{position:absolute;font-size:9.8px;line-height:14.4px}
.list .row{display:flex;justify-content:space-between;gap:6px}
.list .row span:last-child{font-weight:600;white-space:nowrap}
.flavors{position:absolute;left:304px;top:450px;width:211px;height:52px;background:var(--blue-mid);padding:7px 10px;font-size:9.5px;line-height:14px}
.flavors .row{display:flex;justify-content:space-between;font-weight:700}
</style>
</head>
<body>

<!-- ============ BREAKFAST PANEL ============ -->
<section class="panel panel--breakfast">
  <header class="masthead">
    <span class="brand-mark"></span>
    <span class="brand-name">Brise De Lavande</span>
    <h1 class="title"><span class="l1">FRENCH BAKERY</span><span class="l2">AND CAFE</span></h1>
  </header>
  <div class="band"></div>

  <div class="frame" style="left:24px;top:189px;width:512px;height:566px"></div>
  <h2 class="script" style="left:279px;top:188px">Breakfast</h2>

  <div class="it" style="left:52px;top:210px"><h4><span>Le Benedicts</span><span></span></h4>
    <p>two poached eggs, lemon herb hollandaise, English muffin</p>
    <p class="sub" style="margin-top:7px;justify-content:space-between"><span><b>classic:</b> canadian bacon</span><b>$11</b></p>
    <p class="sub" style="margin-top:6px;justify-content:space-between"><span><b>salmon:</b> smoked salmon &amp; tomato</span><b>$14</b></p></div>
  <div class="it" style="left:52px;top:297px"><h4><span>Blt &amp; Avocado Omelette</span><span>$12</span></h4>
    <p>bacon, arugula, tomato, avocado, cheddar, lemon herb hollandaise</p></div>
  <div class="it" style="left:52px;top:347px"><h4><span>Pesto Omelette</span><span>$13</span></h4>
    <p>roasted red peppers, caramelized onions, chevre, pesto</p></div>
  <div class="it" style="left:52px;top:397px"><h4><span>Build Your Own Three<br>Egg Omelette</span><span>$5.95</span></h4>
    <p><b>Egg white only +$.80</b><br>brie $1.35, goat cheese $1.35, swiss $1.35, cheddar $1.35, ham $1.50, chicken sausage $3.00, bacon $2.50, spinach $.85, tomatoes $.85, mushrooms $.85, green onions $.85, red peppers $.85</p></div>
  <div class="it" style="left:52px;top:512px"><h4><span>Eggs Croissant</span><span>$8</span></h4>
    <p>two scrambled eggs with Swiss cheese served in a croissant.</p>
    <p style="margin-top:6px">ham $1.50, chicken Sausage $2.00, bacon $1.50,spinach $.85, tomato $.85</p></div>
  <div class="it" style="left:52px;top:594px"><h4><span>Fried Egg BLT</span><span>$11</span></h4>
    <p>soft fried egg, bacon, lettuce, tomato, avocado, toasted croissant</p></div>
  <div class="it" style="left:52px;top:644px"><h4><span>Monte Cristo</span><span>$12</span></h4>
    <p>french toast, ham, swiss, bechamel, raspberry jam, fried easy egg +$1.00</p></div>
  <div class="it" style="left:52px;top:693px"><h4><span>Parmesan Polenta Bowl</span><span>$12</span></h4>
    <p style="margin-top:2px">creamy polenta, parmesan, with chicken sausage, shallots, roasted red peppers</p></div>

  <div class="it" style="left:297px;top:210px"><h4><span>Quiches</span><span>$10</span></h4>
    <p style="margin-top:5px"><b>Lorraine:</b> ham, bacon &amp; swiss cheese</p>
    <p style="margin-top:4px"><b>spinach:</b> spinach &amp; swiss cheese</p></div>
  <div class="it" style="left:297px;top:272px"><h4><span>Yogurt &amp; Granola Parfait</span><span>$8</span></h4>
    <p>vanilla greek yogurt, local honey, seasonal fruit, house made almond granola</p></div>
  <div class="it" style="left:297px;top:322px"><h4><span>The Grande Breakfast</span><span>$15</span></h4>
    <p>Two eggs any style, bacon or chicken sausage, croissant or baguette, choice of hashbrowns, roasted potatoes, fruit</p></div>
  <div class="it" style="left:297px;top:384px"><h4><span>Avocado Tartine</span><span>$11</span></h4>
    <p>avocado, pickled red onion, dijonaise, chili raisins, alfalfa sprouts, multigrain, Marelle salt</p></div>
  <div class="it" style="left:297px;top:446px"><h4><span>Smoked Salmon Tartine</span><span>$14</span></h4>
    <p>truffled scrambled eggs, smoked salmon, pickled red onion, caper berries, cucumber, tomato, arugula, multigrain, herbed cream cheese</p></div>
  <div class="it" style="left:297px;top:522px"><h4><span>Crepe Du Jour</span><span>$9</span></h4>
    <p class="sub" style="margin-top:5px"><b>sweet:</b><span>classic crepe, strawberry, banana, chocolate ganache or Noisella</span></p>
    <p class="sub" style="margin-top:7px"><b>savory:</b><span>buckwheat crepe, cheddar, bacon, fried egg</span></p>
    <p class="sub" style="margin-top:7px"><b>savory:</b><span>ham &amp; swiss stuffed crepe, fried easy egg</span></p></div>
  <div class="it" style="left:297px;top:650px"><h4><span>Crème Brulee French Toast</span><span>$11</span></h4>
    <p>crème brulee soaked brioche, blueberry compote, crème anglaise</p></div>
  <div class="it" style="left:297px;top:707px"><h4><span>Belgium Waffle</span><span>$10</span></h4>
    <p>biscotin butter, roasted pecan maple syrup</p></div>

  <h2 class="script" style="left:280px;top:789px;background:none">Soups and Salads</h2>

  <div class="it" style="left:52px;top:815px"><h4><span>Tomato Basil Soup</span><span>cup $4<br>bowl $8</span></h4>
    <p style="margin-top:-12px">tomato, basil, cream, croutons</p></div>
  <div class="it" style="left:52px;top:851px"><h4><span>Soup Du Jour</span><span>cup $4<br>bowl $8</span></h4>
    <p style="margin-top:-12px;width:150px">ask your server for our soup of the day with our homemade croutons</p></div>
  <div class="it" style="left:52px;top:912px"><h4><span>Garden Salad</span><span>sm $5<br>lg $10</span></h4>
    <p style="margin-top:-12px;width:165px">baby lettuces, english cucumbers, cherry tomato, marinated feta, french vinaigrette</p></div>
  <div class="it" style="left:297px;top:815px"><h4><span>Caesar Salad</span><span>sm $5<br>lg $10</span></h4>
    <p style="margin-top:-12px;width:165px">romaine, parmesan, brioche croutons, lemon parmesan dressing</p></div>
  <div class="it" style="left:297px;top:864px"><h4><span>Marinated Beet Salad</span><span>$14</span></h4>
    <p>smoked blue cheese crumbles, balsamic &amp; candied pecans</p></div>
  <div class="it" style="left:297px;top:913px"><h4><span>Salmon Atlantique</span><span>$14</span></h4>
    <p>mixed greens, smoked salmon, golden raisins, walnuts,goat cheese with balsamic dressing</p></div>

  <svg class="waves" viewBox="0 0 560 140" aria-hidden="true">
    <defs><linearGradient id="wb1" x1="0" y1="0" x2="1" y2="0"><stop offset="0" stop-color="#0677ba"/><stop offset=".5" stop-color="#7badd7"/><stop offset="1" stop-color="#0054aa"/></linearGradient></defs>
    <path d="M0 78 C150 48 300 98 420 80 C480 70 530 45 560 25 L560 90 C470 130 300 138 150 122 C90 117 40 120 0 132 Z" fill="url(#wb1)"/>
    <path d="M0 64 C150 34 300 76 420 60 C480 52 530 28 560 8 L560 26 C520 50 470 74 410 82 C290 98 150 60 0 82 Z" fill="#eb3d1f"/>
  </svg>
  <p class="fine">We politely decline menu modifications and substitutions, thank you for understanding.<br>**EGGS MAY BE COOKED TO ORDER *** THE CONSUMPTION OF RAW OR UNDERCOOKED EGGS, HAMBURGERS, SHELLFISH, POULTRY,<br>FISH AND STEAK MAYINCREASE YOUR RISK OF FOOD BORN ILLNESS, ESPECIALLY IF YOU HAVE CERTAIN MEDICAL CONDITIONS.</p>
</section>

<!-- ============ LUNCH PANEL ============ -->
<section class="panel panel--lunch">
  <header class="masthead">
    <span class="brand-mark"></span>
    <span class="brand-name">Brise De Lavande</span>
    <h1 class="title"><span class="l1">FRENCH BAKERY</span><span class="l2">AND CAFE</span></h1>
  </header>
  <div class="band"></div>

  <h2 class="script script--plain" style="left:52px;top:188px">Sandwiches</h2>
  <div class="photo photo--pie" role="img" aria-label="Photo of a golden chicken pot pie with flaky pastry on a white plate"></div>

  <div class="it" style="left:52px;top:223px"><h4><span>Jambon Beurre Fromage<br>Baguette</span><span>cup $6<br>bowl $10</span></h4>
    <p>black forest ham, swiss cheese, butter, whole, baguette.</p></div>
  <div class="it" style="left:52px;top:286px"><h4><span>Chicken Salad</span><span>$10</span></h4>
    <p>lemon tarragon roast chicken, apples, bibb lettuce, on your choice of butter croissant or baguette.</p></div>
  <div class="it" style="left:52px;top:350px"><h4><span>Frenchie</span><span>cup $6<br>bowl $10</span></h4>
    <p style="margin-top:-12px;width:150px">brie, lettuce, tomato, butter, baguette.</p></div>
  <div class="it" style="left:52px;top:401px"><h4><span>Les Croques</span><span>Msr: $11<br>Mdme: $12</span></h4>
    <p style="margin-top:-12px">black forest ham, swiss cheese,<br>bechamel, pain de mie bread.</p></div>
  <div class="it" style="left:52px;top:453px"><h4><span>Grown Up Grilled Cheese</span><span>$14</span></h4>
    <p>shaved roast beef, pimento cheese, caramelized onion, horseradish crème,brioche, served with house made pickles</p></div>
  <div class="it" style="left:52px;top:524px"><h4><span>Chicken Panini</span><span>$12</span></h4>
    <p>marinated chicken, brie, tomato, red onion marmalade, balsamic glaze, ciabatta.</p></div>
  <div class="it" style="left:52px;top:577px"><h4><span>l’Italiano</span><span>$10</span></h4>
    <p>fresh mozzarella, tomatoes, basil pesto, arugula, balsamic, ciabatta</p></div>
  <div class="photo photo--panini" role="img" aria-label="Photo of a grilled panini with tomato and greens"></div>

  <div class="frame" style="left:284px;top:429px;width:253px;height:310px"></div>
  <h2 class="script" style="left:410px;top:427px">Entrees</h2>
  <div class="it" style="left:305px;top:449px"><h4><span>Tourte au Poulet</span><span>$15</span></h4>
    <p>marinated chicken, swiss cheese, onion, mushroom, bechamel, flaky pastry</p></div>
  <div class="it" style="left:305px;top:513px"><h4><span>Beef Bourguignon</span><span>$18</span></h4>
    <p>red wine braised beef, pearl onions, carrots, mushrooms, buttered egg noodles</p></div>
  <div class="it" style="left:305px;top:564px"><h4><span>Fork &amp; Knife “French Dip”<br>Tartine</span><span>$16</span></h4>
    <p>shaved roast beef, arugula, smoked blue cheese, horseradish crème, pickled onions &amp; au jus</p></div>
  <div class="it" style="left:305px;top:646px"><h4><span>Ratatouille &amp; eggs</span><span>$14</span></h4>
    <p>roasted squash, peppers, eggplant, tomatoes, freshherbs, choice of two eggs &amp; a side of baguette<br>add bacon, chicken sausage, or andouille sausage +$5</p></div>

  <div class="frame" style="left:22px;top:780px;width:253px;height:178px"></div>
  <h2 class="script" style="left:148px;top:778px">Sides</h2>
  <div class="side" style="top:803px"><span>fruit salad | roasted potatoes |<br>hash brown $3</span><b>$3</b></div>
  <div class="side" style="top:840px"><span>bacon | chicken sausage |<br>andouille sausage $5</span><b>$5</b></div>
  <div class="side" style="top:876px"><span>haricot vert with shallot fresh<br>corn &amp;andouille sausage $7</span><b>$7</b></div>
  <div class="side" style="top:913px"><span>roasted brussel sprouts, dried<br>cranberries, balsamic</span><b>$6</b></div>

  <div class="kids-head">
    <h2 class="script">Kids Menu</h2>
    <span class="kids-price">$7</span>
  </div>
  <ul class="kids-list">
    <li>French toast with maple syrup</li>
    <li>Scrambled eggs &amp; bacon platter</li>
    <li>Egg &amp; cheese breakfast sandwich</li>
    <li>Strawberry &amp; Noisella crepe</li>
    <li>Yogurt and berries</li>
    <li>Grilled cheese sandwich</li>
    <li>*All meals served with fruit</li>
    <li>or potatoes</li>
  </ul>

  <svg class="waves" viewBox="0 0 560 140" aria-hidden="true">
    <defs><linearGradient id="wb2" x1="0" y1="0" x2="1" y2="0"><stop offset="0" stop-color="#0677ba"/><stop offset=".5" stop-color="#7badd7"/><stop offset="1" stop-color="#0054aa"/></linearGradient></defs>
    <path d="M0 78 C150 48 300 98 420 80 C480 70 530 45 560 25 L560 90 C470 130 300 138 150 122 C90 117 40 120 0 132 Z" fill="url(#wb2)"/>
    <path d="M0 64 C150 34 300 76 420 60 C480 52 530 28 560 8 L560 26 C520 50 470 74 410 82 C290 98 150 60 0 82 Z" fill="#eb3d1f"/>
  </svg>
  <p class="fine">We politely decline menu modifications and substitutions, thank you for understanding.<br>**EGGS MAY BE COOKED TO ORDER *** THE CONSUMPTION OF RAW OR UNDERCOOKED EGGS, HAMBURGERS, SHELLFISH, POULTRY,<br>FISH AND STEAK MAYINCREASE YOUR RISK OF FOOD BORN ILLNESS, ESPECIALLY IF YOU HAVE CERTAIN MEDICAL CONDITIONS.</p>
</section>

<!-- ============ DRINKS PANEL ============ -->
<section class="panel panel--drinks">
  <header class="masthead">
    <span class="brand-mark"></span>
    <span class="brand-name">Brise De Lavande</span>
    <h1 class="title"><span class="l1">FRENCH BAKERY</span><span class="l2">AND CAFE</span></h1>
  </header>
  <div class="band"></div>

  <h3 class="head" style="left:52px;top:180px">REDS</h3>
  <span class="rule" style="left:52px;top:200px"></span>
  <div class="wine" style="top:198px">
    <div class="row cols"><span></span><span>Glass</span><span>Bottle</span></div>
    <div class="row" style="margin-top:1px"><span>Château Bellerive Cabernet Sauvignon</span><span>$9</span><span>$34</span></div>
    <div class="row"><span>Le Petit Corbeau Pinot Noir</span><span>$9</span><span>$36</span></div>
  </div>

  <h3 class="head" style="left:52px;top:269px">WHITES + ROSE</h3>
  <span class="rule" style="left:52px;top:290px"></span>
  <div class="wine" style="top:286px">
    <div class="row cols"><span></span><span>Glass</span><span>Bottle</span></div>
    <div class="row" style="margin-top:2px"><span>Domaine Vieilles Pierres Rose</span><span>$8</span><span>$32</span></div>
    <div class="row"><span>Coteaux Ardoise Chardonnay</span><span>$9</span><span>$36</span></div>
    <div class="row"><span>Alain Morel Sauvignon Blanc</span><span>$8</span><span>$32</span></div>
    <div class="row"><span>Estate Riesling</span><span>$8</span><span>$32</span></div>
    <div class="row"><span>Villa Santa Rosa Pinot Grigio</span><span>$8</span><span>$32</span></div>
  </div>

  <h3 class="head" style="left:52px;top:385px">BUBBLES</h3>
  <div class="wine" style="top:402px">
    <div class="row cols"><span></span><span>Glass</span><span>Bottle</span></div>
    <div class="row" style="margin-top:2px"><span>Maison Delorme Cremant de Bourgogne Brut (NV)</span><span>$12</span><span>$48</span></div>
    <div class="row"><span>Clos Chantelune Cremant de Loire Brut Rose</span><span>$14</span><span>$56</span></div>
    <div class="row"><span>Pierre Lucas Blanc de Blanc</span><span>$9</span><span>$36</span></div>
  </div>
  <div class="photo photo--wine" role="img" aria-label="Photo of a glass of white wine with grapes in a vineyard"></div>

  <div class="frame" style="left:23px;top:617px;width:253px;height:346px"></div>
  <h3 class="head head--center" style="left:150px;top:608px">COCKTAILS</h3>
  <div class="stack" style="left:46px;top:634px;width:210px">
    <div class="it"><h4><span>Mimosa</span><span>$10</span></h4>
      <p>champagne, orange juice or cranberry juice</p></div>
    <div class="it"><h4><span>Peach Bellini</span><span>$9</span></h4>
      <p>champagne, peach puree</p></div>
    <div class="it"><h4><span>Apple Cider-Mimosa</span><span>$9</span></h4>
      <p>champagne, apple cider, caramel rim, with brown sugar</p></div>
    <div class="it"><h4><span>Blood Orange or Pineapple Spritz</span><span>$12</span></h4>
      <p>riverline vodka, sweet vermouth, sugar cube, source claire with your choice of flavored puree.</p></div>
    <div class="it"><h4><span>Bloody Mary</span><span>$11</span></h4>
      <p>riverline vodka, fat &amp; juicy bloody mary mix, celery</p></div>
    <div class="it"><h4><span>Espresso Martini</span><span>$10</span></h4>
      <p>espresso shot, chocolate martini, chocolate syrup</p></div>
    <div class="it"><h4><span>Chocolate Coffee Bomb</span><span>$8</span></h4>
      <p>coffee, chocolate martini, whipped cream</p></div>
  </div>

  <div class="frame" style="left:284px;top:189px;width:252px;height:371px"></div>
  <h3 class="head head--center" style="left:410px;top:180px">COFFEES</h3>
  <div class="list" style="left:304px;top:209px;width:211px">
    <div class="row"><span>Café Lumière coffee</span><span>$3</span></div>
    <div class="row"><span>Café Lumière espresso</span><span>$3.50</span></div>
    <div class="row"><span>Americano</span><span>$3.50</span></div>
    <div class="row"><span>Cappuccino</span><span>$4</span></div>
    <div class="row"><span>Latte</span><span>$4</span></div>
    <div class="row"><span>Café Mocha</span><span>$4.50</span></div>
    <div class="row"><span>Café White Mocha</span><span>$4.50</span></div>
    <div class="row"><span>Chai Latte</span><span>$6</span></div>
    <div class="row"><span>Dirty Chai Latte</span><span>$6</span></div>
    <div class="row"><span>Truffle Latte</span><span>$6</span></div>
    <div class="row"><span>Napoleon Latte</span><span>$6</span></div>
    <div class="row"><span>Barraquito</span><span>$4.75</span></div>
    <div class="row"><span>White Chocolate Pumpkin Spice Latte</span><span>$6</span></div>
    <div class="row"><span>(seasonal)</span><span></span></div>
    <div class="row"><span>Hot Cinnamon Vanilla Cider</span><span>$3</span></div>
    <div class="row"><span>Hot Cocoa</span><span>$4</span></div>
  </div>
  <div class="flavors">
    <div class="row"><span>FLAVORS:</span><span>$50</span></div>
    <div>Vanilla, Salted Caramel, Hazelnut, Chocolate, White Chocolate, Lavender</div>
  </div>
  <div class="list" style="left:304px;top:516px;width:211px">
    <div class="row"><span>MILK ALTERNATIVES: Almond, Oat</span><span>$50</span></div>
    <div class="row"><span>Extra Shot</span><span>$1</span></div>
  </div>

  <h3 class="head" style="left:297px;top:581px">BEVERAGES</h3>
  <div class="list" style="left:297px;top:612px;width:210px">
    <div class="row"><span>CANS SODA: Cola, Diet Cola,</span><span>$2.50</span></div>
    <div class="row"><span>Lemon-Lime, Cola Zero</span><span></span></div>
    <div class="row"><span>Orchard Juices assorted flavors</span><span>$4.25</span></div>
    <div class="row"><span>Santa Fonte Blood Orange flavor</span><span>$3.50</span></div>
    <div class="row"><span>Belmare’s <i>assorted flavors</i></span><span>Sm: $4.50</span></div>
    <div class="row"><span></span><span>Lg: $6.50</span></div>
    <div class="row"><span>Source Claire</span><span>$2.50</span></div>
    <div class="row"><span>Val de Loirette <i>assorted flavors</i></span><span>$7</span></div>
    <div class="row"><span>Isla water</span><span>$3.50</span></div>
    <div class="row"><span>Iced Tea</span><span>$2.50</span></div>
    <div class="row"><span>Harbor Peach Tea</span><span>$3.50</span></div>
    <div class="row"><span>Sunbrook <i>assorted flavors</i></span><span>$3.50</span></div>
    <div class="row"><span>Juice: Cranberry, Orange</span><span>$3</span></div>
    <div class="row"><span>Milk, Chocolate Milk</span><span>$2.50</span></div>
  </div>
  <div class="photo photo--juice" role="img" aria-label="Photo of colourful fruit juices with fresh fruit"></div>

  <svg class="waves" viewBox="0 0 560 140" aria-hidden="true">
    <defs><linearGradient id="wb3" x1="0" y1="0" x2="1" y2="0"><stop offset="0" stop-color="#0677ba"/><stop offset=".5" stop-color="#7badd7"/><stop offset="1" stop-color="#0054aa"/></linearGradient></defs>
    <path d="M0 78 C150 48 300 98 420 80 C480 70 530 45 560 25 L560 90 C470 130 300 138 150 122 C90 117 40 120 0 132 Z" fill="url(#wb3)"/>
    <path d="M0 64 C150 34 300 76 420 60 C480 52 530 28 560 8 L560 26 C520 50 470 74 410 82 C290 98 150 60 0 82 Z" fill="#eb3d1f"/>
  </svg>
  <p class="fine">We politely decline menu modifications and substitutions, thank you for understanding.<br>**EGGS MAY BE COOKED TO ORDER *** THE CONSUMPTION OF RAW OR UNDERCOOKED EGGS, HAMBURGERS, SHELLFISH, POULTRY,<br>FISH AND STEAK MAYINCREASE YOUR RISK OF FOOD BORN ILLNESS, ESPECIALLY IF YOU HAVE CERTAIN MEDICAL CONDITIONS.</p>
</section>

</body>
</html>
```